Charity website needing new website design

Hi there. We are looking to get a revamped website for our non for profit charity. We specialise in eye cataract surgeries and ear care around the world. Please visit our website brightcareaid.org.au for the current layout.
I have attached a brief with photos. The about us page please include an interactive map showing our locations we operate in. The website should be easy to use, match our logo design and be clear to navigate. Pixvault and other images can be used if they fit the scheme of the website and feel. The donation page should incorporate the gateway to receive donations. The team page should have each photo of the team member next to it. Please compare to other charity websites such as ORANTA, Global Haven etc. Another website which has a lovely and easy to use scheme is tkqhaustralia.org.au
The tabs should be in the following order:
About us, Why Health? Our Team, Eye Care Programs, Ear Care Programs, Contact Us, Donate.
Please make sure the website is both compatible with mobile & computer.
The Listed Benefactor Badge can be at the footer of the page with details of brightcare etc

```html
<!DOCTYPE html>
<html lang="en">
<head>
<meta charset="utf-8">
<title>Brightcare Aid Foundation</title>
<link href="https://fonts.googleapis.com/css2?family=Poppins:wght@400;500;600&display=swap" rel="stylesheet">
<style>
:root{
  --green:#3db56c;
  --green-soft:#eef7f1;
  --navy:#1c2b4a;
  --navy-deep:#262b4d;
  --teal-bar:#0f3a4a;
  --orange:#f5a623;
  --text:#3b4256;
  --muted:#6b7285;
  --line:#e3e6ea;
  --white:#ffffff;
}
*{box-sizing:border-box;margin:0;padding:0}
html,body{width:1200px;height:4478px;overflow:hidden}
body{position:relative;font-family:"Poppins",sans-serif;color:var(--text);background:var(--white)}
.abs{position:absolute}
a{color:inherit;text-decoration:none}
.btn{display:inline-flex;align-items:center;justify-content:center;gap:6px;font-size:16px;font-weight:500;border-radius:3px}
.btn-green{background:var(--green);color:var(--white)}
.btn-outline{border:2px solid var(--navy);color:var(--navy);background:var(--white)}
.photo{border-radius:4px}

/* top bar */
.topbar{left:0;top:0;width:1200px;height:42px;background:var(--teal-bar);color:#cfe3e6;font-size:11px}
.topbar .contact{left:83px;top:13px;display:flex;gap:14px}
.topbar .social{right:83px;top:11px;display:flex;gap:8px}
.dot{width:20px;height:20px;border-radius:50%;background:var(--green)}

/* nav */
.brand{display:flex;align-items:center;gap:10px}
.brand .mark{width:34px;height:34px;border-radius:50%;background:var(--green)}
.brand .name{font-size:19px;font-weight:600;color:var(--navy);line-height:1}
.brand .name small{display:block;font-size:10px;font-weight:500;letter-spacing:2px;margin-top:3px}
.nav{left:83px;top:60px;width:1037px;display:flex;justify-content:space-between;align-items:center}
.nav ul{display:flex;gap:34px;list-style:none;font-size:13px;color:var(--navy)}
.nav li.active{color:var(--green)}

/* hero */
.hero-title{left:0;top:124px;width:1200px;text-align:center;font-size:54px;font-weight:500;line-height:62px;color:var(--navy)}
.hero-btns{left:0;top:290px;width:1200px;display:flex;justify-content:center;gap:6px}
.hero-btns .btn{width:183px;height:46px}
.hero-photo{left:83px;top:386px;width:1037px;height:501px;background:linear-gradient(120deg,#6b5a48,#a89478 45%,#4b3a2e 70%,#8a7a66)}
.badge{left:104px;top:311px;width:150px;height:150px;border-radius:50%;background:#fff;border:10px solid var(--orange)}
.hero-caption{left:734px;top:753px;width:318px;height:134px;background:rgba(30,30,34,.55);color:#eee;font-size:12px;line-height:20px;padding:14px 14px 10px 16px;overflow:hidden}
.hero-arrow{left:1052px;top:753px;width:68px;height:134px;background:var(--green);display:flex;align-items:center;justify-content:center}

/* stats */
.green-band{left:0;top:1099px;width:1200px;height:529px;background:var(--green-soft)}
.stats{left:83px;top:988px;width:1037px;height:146px;background:#fff;box-shadow:0 4px 24px rgba(0,0,0,.06);display:flex;justify-content:space-around;align-items:center;border-radius:4px}
.stat{display:flex;align-items:center;gap:12px}
.stat .num{font-size:36px;font-weight:600;color:var(--navy);line-height:1}
.stat .num sup{color:var(--green);font-size:24px}
.stat .lbl{font-size:13px;color:var(--navy)}

/* about */
.about-photo{left:0;top:1136px;width:504px;height:492px;background:linear-gradient(135deg,#4a3426,#7b5a3e 50%,#c59a3a)}
.about-title{left:602px;top:1205px;font-size:45px;font-weight:500;color:var(--navy)}
.about-text{left:602px;top:1283px;width:512px;font-size:13px;line-height:21.8px;color:var(--navy)}
.about-btn{left:602px;top:1497px;width:174px;height:47px}

/* programs */
.section-title{left:0;width:1200px;text-align:center;font-size:46px;font-weight:500;line-height:54px;color:var(--navy)}
.card{top:1899px;width:333px;height:475px;background:#fff;box-shadow:0 2px 18px rgba(0,0,0,.07);padding:18px}
.card .img{height:275px;border-radius:2px}
.card h3{font-size:19px;font-weight:500;color:var(--navy);margin-top:32px}
.card p{font-size:13px;line-height:22px;color:var(--muted);margin-top:4px}
.card .btn{width:100%;height:45px;margin-top:12px}

/* support */
.support-band{left:0;top:2499px;width:1200px;height:671px;background:var(--green-soft)}
.support-title{left:83px;top:2588px;width:560px;font-size:37px;font-weight:500;line-height:52px;letter-spacing:-0.3px;color:var(--navy);white-space:nowrap}
.support-text{left:85px;top:2728px;width:440px;font-size:13px;line-height:22px;color:var(--muted)}
.amount-label{left:85px;top:2856px;font-size:19px;font-weight:500;color:var(--navy)}
.amount-input{left:85px;top:2897px;width:421px;height:58px;background:#fff;border-radius:3px;font-size:13px;color:var(--muted);padding:0 24px;display:flex;align-items:center;justify-content:space-between}
.amount-input .cur{background:#e4e6ea;padding:10px 16px;border-radius:3px;margin-right:-16px;color:var(--navy)}
.presets{left:92px;top:2982px;display:flex;gap:9px}
.presets span{width:75px;height:30px;border:1.5px solid var(--navy);border-radius:3px;font-size:13px;display:flex;align-items:center;justify-content:center;color:var(--navy)}
.support-btn{left:87px;top:3040px;width:420px;height:45px}
.support-photo{left:666px;top:2586px;width:458px;height:363px;background:linear-gradient(120deg,#8a8d6a,#c7a33b 40%,#6d5b4a 65%,#c65c7a)}
.progress{left:668px;top:2999px;width:456px;font-size:13px;color:var(--navy)}
.progress .pct{text-align:center;font-weight:600}
.progress .track{height:7px;background:#fff;border-radius:4px;margin-top:10px}
.progress .fill{width:50%;height:7px;background:var(--orange);border-radius:4px}
.progress .row{display:flex;justify-content:space-between;margin-top:14px;line-height:18px}
.progress b{display:block;font-size:19px;font-weight:600;color:var(--green)}
.progress .togo b{color:var(--orange)}

/* stories */
.stories{left:0;top:3390px;width:1200px;height:316px;display:flex}
.story{position:relative;width:400px;height:316px;color:#fff}
.story h4{position:absolute;left:84px;font-size:19px;font-weight:500;line-height:28px}
.story p{position:absolute;left:84px;top:183px;width:230px;font-size:13px;line-height:21px;color:#dfe2ee}
.story .plus{position:absolute;right:0;bottom:0;width:38px;height:38px;background:var(--green);display:flex;align-items:center;justify-content:center}

/* cta + footer */
.footer{left:0;top:4031px;width:1200px;height:447px;background:var(--navy-deep);color:#c9cce0}
.cta{left:83px;top:3834px;width:1037px;height:314px;background:var(--green);text-align:center}
.cta h2{margin-top:68px;font-size:43px;font-weight:500;line-height:54px;color:#fff}
.cta .btn{margin-top:26px;width:182px;height:44px;background:var(--orange);color:#fff}
.foot-brand .name{color:#fff}
.foot-col{font-size:13px;color:#c9cce0}
.foot-col h5{font-size:13px;font-weight:600;color:#fff;margin-bottom:18px;line-height:21px}
.foot-col li{list-style:none;line-height:24px}
.foot-email{width:256px;height:44px;border:1px solid #8a8fae;border-radius:3px;padding:0 18px;display:flex;align-items:center;font-size:13px}
.foot-sub{margin-top:22px;width:165px;height:44px;border:2px solid var(--green);color:var(--green)}
.legal{left:83px;top:4417px;width:1037px;border-top:1px solid #474c6c;padding-top:22px;display:flex;justify-content:space-between;font-size:12px;color:#9a9eb8}
</style>
</head>
<body>

<div class="abs topbar">
  <div class="abs contact"><span>&#9742; 10 555 210 448</span><span>|</span><span>&#9993; info@brightcareaid.org.au</span></div>
  <div class="abs social"><span class="dot"></span><span class="dot"></span><span class="dot"></span><span class="dot"></span></div>
</div>

<nav class="abs nav">
  <div class="brand"><span class="mark"></span><span class="name">BRIGHTCARE AID<small>FOUNDATION</small></span></div>
  <ul><li class="active">Home</li><li>About Us</li><li>Why Health?</li><li>Our Team</li><li>Eye Care Programs</li><li>Contact Us</li></ul>
</nav>

<h1 class="abs hero-title">Help bring basic health care to<br>every person on the planet.</h1>
<div class="abs hero-btns"><a class="btn btn-green">Donate Now &rarr;</a><a class="btn btn-outline">Learn More &rarr;</a></div>
<div class="abs hero-photo photo" role="img" aria-label="Photo of smiling children in a village"></div>
<div class="abs badge" role="img" aria-label="Listed Benefactor Badge"></div>
<div class="abs hero-caption">Through symbiotic health programs brightcare aid foundation provides innovative solutions to Eye and Hearing Health in the developing world with an ethical professional and sustainable approach.</div>
<div class="abs hero-arrow"><svg width="28" height="28" viewBox="0 0 24 24" fill="none" stroke="#fff" stroke-width="2"><path d="M4 12h16M13 5l7 7-7 7"/></svg></div>

<div class="abs green-band"></div>
<div class="abs stats">
  <div class="stat"><svg width="48" height="48" viewBox="0 0 48 48" fill="none" stroke="#3db56c" stroke-width="2"><circle cx="24" cy="14" r="7"/><path d="M10 42c0-9 6-15 14-15s14 6 14 15z"/></svg><div><div class="num">10,000<sup> +</sup></div><div class="lbl">Lives Impacted</div></div></div>
  <div class="stat"><svg width="48" height="48" viewBox="0 0 48 48" fill="none" stroke="#3db56c" stroke-width="2"><path d="M8 44V24l6-8 4 6v22M30 44V22l4-6 6 8v20M18 30h12"/></svg><div><div class="num">500<sup> +</sup></div><div class="lbl">Volunteers Engaged</div></div></div>
  <div class="stat"><svg width="48" height="48" viewBox="0 0 48 48" fill="none" stroke="#3db56c" stroke-width="2"><path d="M24 4l14 6v12c0 10-6 18-14 22C16 40 10 32 10 22V10z"/><path d="M17 24l5 5 9-10"/></svg><div><div class="num">$1 Million</div><div class="lbl">Raised for Causes</div></div></div>
  <div class="stat"><svg width="48" height="48" viewBox="0 0 48 48" fill="none" stroke="#3db56c" stroke-width="2"><circle cx="28" cy="18" r="12"/><path d="M28 11v7l5 3M4 38l10-8h12l-8 6 14-4"/></svg><div><div class="num">15 Years</div><div class="lbl">of Dedicated Service</div></div></div>
</div>

<div class="abs about-photo" role="img" aria-label="Photo of children looking through a wooden window"></div>
<h2 class="abs about-title">About Us</h2>
<p class="abs about-text">Brightcare Aid Foundation is dedicated to improving and transforming the lives of people through enhanced vision and hearing health in the developing world. Our mission is to bridge the gap in access to essential eye and hearing care, ensuring that everyone, regardless of their circumstances, has the opportunity to see and hear clearly. With over 70 years of humanitarian aid across our members, we are passionate to provide innovative, sustainable, ethical and professional symbiotic solutions across multiple health programs.</p>
<a class="abs btn btn-green about-btn">Learn More &rarr;</a>

<h2 class="abs section-title" style="top:1743px">Contribute to improving<br>global healthcare access</h2>
<div class="abs card" style="left:83px"><div class="img" role="img" aria-label="Photo of an eye care examination" style="background:linear-gradient(135deg,#8c8f94,#cfd0cc 50%,#6e6a66)"></div><h3>Eye Care</h3><p>Nunc mattis enim ut tellus elementum. Porta nibh venenatis cras sed felis eget velit aliquet. Aliquam purus sit amet luctus.</p><a class="btn btn-outline">Donate Now &rarr;</a></div>
<div class="abs card" style="left:435px"><div class="img" role="img" aria-label="Photo of a man touching his ear" style="background:linear-gradient(135deg,#2f2420,#6b4a38 55%,#3a2c26)"></div><h3>Ear Care</h3><p>Nunc mattis enim ut tellus elementum. Porta nibh venenatis cras sed felis eget velit aliquet. Aliquam purus sit amet luctus.</p><a class="btn btn-green">Donate Now &rarr;</a></div>
<div class="abs card" style="left:786px"><div class="img" role="img" aria-label="Photo of a health worker assisting a woman" style="background:linear-gradient(135deg,#3f6fa8,#8a7a6a 50%,#4a3b33)"></div><h3>General Health</h3><p>Nunc mattis enim ut tellus elementum. Porta nibh venenatis cras sed felis eget velit aliquet. Aliquam purus sit amet luctus.</p><a class="btn btn-outline">Donate Now &rarr;</a></div>

<div class="abs support-band"></div>
<h2 class="abs support-title">Support children in reaching<br>their maximum capabilities.</h2>
<p class="abs support-text">We work tirelessly to ensure that children have access to quality education, regardless of their background. Our initiatives range from building schools in underserved communities to providing scholarships and educational materials.</p>
<div class="abs amount-label">Donation Amount</div>
<div class="abs amount-input"><span>$ 60</span><span class="cur">USD &#8964;</span></div>
<div class="abs presets"><span>$10</span><span>$50</span><span>$100</span><span>$150</span><span>$200</span></div>
<a class="abs btn btn-green support-btn">Donate Now &rarr;</a>
<div class="abs support-photo photo" role="img" aria-label="Photo of a smiling girl with a young man behind her"></div>
<div class="abs progress">
  <div class="pct">50%</div>
  <div class="track"><div class="fill"></div></div>
  <div class="row"><div>Goal<b>$40,000</b></div><div>Raised<b>$20,000</b></div><div class="togo">To go<b>$20,000</b></div></div>
</div>

<h2 class="abs section-title" style="top:3286px">Building a Brighter Future</h2>
<div class="abs stories">
  <div class="story" role="img" aria-label="Photo of a community gathering" style="background:linear-gradient(135deg,#3c4566,#5a5f7a 60%,#6e6650)"><h4 style="top:214px">Lorem ipsum dolor sit<br>amet, consectetur</h4><span class="plus"><svg width="20" height="20" viewBox="0 0 20 20" stroke="#fff" stroke-width="2"><path d="M10 3v14M3 10h14"/></svg></span></div>
  <div class="story" style="background:var(--navy-deep)"><h4 style="top:120px">Lorem ipsum dolor sit<br>amet, consectetur</h4><p>Nullam at tellus maximus, feugiat turpis ac, faucibus eros. Quisque pulvinar lorem ac nulla varius ultricies.</p><span class="plus"><svg width="18" height="18" viewBox="0 0 20 20" stroke="#fff" stroke-width="2"><path d="M4 4l12 12M16 4L4 16"/></svg></span></div>
  <div class="story" role="img" aria-label="Photo of a mother carrying a child" style="background:linear-gradient(135deg,#3a3d5a,#4d4560 55%,#5a3f3a)"><h4 style="top:214px">Lorem ipsum dolor sit<br>amet, consectetur</h4><span class="plus"><svg width="20" height="20" viewBox="0 0 20 20" stroke="#fff" stroke-width="2"><path d="M10 3v14M3 10h14"/></svg></span></div>
</div>

<footer class="abs footer"></footer>
<div class="abs cta"><h2>Partner with Brightcare Aid to make a<br>positive difference starting today.</h2><a class="btn">Donate Now &rarr;</a></div>

<div class="abs brand foot-brand" style="left:83px;top:4198px"><span class="mark"></span><span class="name">BRIGHTCARE AID<small>FOUNDATION</small></span></div>
<div class="abs" style="left:85px;top:4266px;display:flex;gap:9px"><span class="dot"></span><span class="dot"></span><span class="dot"></span><span class="dot"></span></div>
<div class="abs foot-col" style="left:362px;top:4210px"><h5>Contacts</h5><ul><li><span style="color:var(--green)">&#9679;</span>&nbsp; 10 555 210 448</li><li style="margin-top:10px"><span style="color:var(--green)">&#9679;</span>&nbsp; info@brightcareaid.org.au</li></ul></div>
<div class="abs foot-col" style="left:656px;top:4210px"><h5>Main Menu</h5><ul><li>Home</li><li>About Us</li><li>Why Health?</li><li>Our Team</li><li>Contact Us</li></ul></div>
<div class="abs foot-col" style="left:859px;top:4210px"><h5>Subscribe to our newsletter and<br>stay updated!</h5><div class="foot-email">Email</div><a class="btn foot-sub">Subscribe &rarr;</a></div>
<div class="abs legal"><span>&copy; 2024 Brightcare Aid. All rights reserved.</span><span>Privacy Policy | Terms of Use</span></div>

</body>
</html>
```